Packaging Design New Cosmetics Range

Small Establish online Beauty company is expanding it's product range into Serums, Sprays and Creams . We are looking for a new fresh packaging design for this launch.
We only use products that are Organic , Not Tested on Animals and Natural products
We would be interested in viewing a White Design , Black design and a designer choice of colors .
First Products are
Rose Water in 100ml glass bottle with box
and a set of 3 Face Serums Vit C , Retinol and Hyaluronic in 30ml Glass bottle = Box
Scrubs and creams will launch later in Q1 2020 however would like a similar feel across all products
Target Market(s)
SEA / US Markets
Industry/Entity Type
Cosmetics
Colors
Designer to choose colors to be used in the design.
Requirements
Must have
- Space Allocated for Product Use and Bar Codes on Box
Nice to have
- Organic , Not tested on animal Logo's

```html
<!DOCTYPE html>
<html lang="en">
<head>
<meta charset="UTF-8">
<title>Rose Water Label</title>
<link href="https://fonts.googleapis.com/css2?family=Kaushan+Script&family=Montserrat:wght@300&display=swap" rel="stylesheet">
<style>
  :root {
    --page-bg: #f1f2f2;
    --teal: #14ad93;
    --teal-deep: #2f9c86;
    --frame: #3b3b3d;
    --white: #ffffff;
    --rose-red: #c4182a;
    --leaf-green: #2f5a2c;
  }
  html, body {
    margin: 0;
    padding: 0;
    width: 1200px;
    height: 2535px;
    overflow: hidden;
    background: var(--page-bg);
  }
  .canvas {
    position: relative;
    width: 1200px;
    height: 2535px;
  }
  .label {
    position: absolute;
    left: 100px;
    top: 767px;
    width: 1000px;
    height: 1000px;
    overflow: hidden;
    background: linear-gradient(180deg, var(--teal) 0%, var(--teal) 55%, var(--teal-deep) 100%);
    box-shadow: 0 6px 18px rgba(0,0,0,0.18);
  }
  .label-frame {
    position: absolute;
    inset: 0;
  }
  .rose-illustration {
    position: absolute;
    left: 200px;
    top: 440px;
    width: 800px;
    height: 560px;
    background:
      radial-gradient(ellipse 230px 200px at 62% 58%, var(--rose-red) 0%, rgba(196,24,42,0.85) 60%, rgba(196,24,42,0) 100%),
      radial-gradient(ellipse 420px 300px at 60% 60%, rgba(47,90,44,0.75) 0%, rgba(47,90,44,0) 100%);
  }
  .brand {
    position: absolute;
    left: 660px;
    top: 150px;
    width: 220px;
    text-align: center;
    color: var(--white);
    font-family: "Montserrat", sans-serif;
    font-weight: 300;
  }
  .brand-mark {
    display: block;
    width: 64px;
    height: 64px;
    margin: 0 auto 10px;
    border: 3px solid var(--white);
    border-radius: 50%;
  }
  .brand-name {
    font-size: 72px;
    line-height: 1;
    letter-spacing: 1px;
  }
  .product-name {
    position: absolute;
    left: 160px;
    top: 255px;
    margin: 0;
    font-family: "Kaushan Script", cursive;
    font-weight: 400;
    font-size: 290px;
    line-height: 1;
    color: var(--white);
    text-shadow: 2px 4px 10px rgba(0,0,0,0.15);
  }
  .product-type {
    position: absolute;
    left: 178px;
    top: 538px;
    font-family: "Kaushan Script", cursive;
    font-size: 80px;
    line-height: 1;
    color: var(--white);
  }
  .volume-tab {
    position: absolute;
    left: 0;
    top: 680px;
    width: 222px;
    height: 92px;
    background: var(--white);
    border-top-right-radius: 46px;
    display: flex;
    align-items: center;
    padding-left: 50px;
    box-sizing: border-box;
    font-family: "Kaushan Script", cursive;
    font-size: 46px;
    color: var(--teal);
  }
</style>
</head>
<body>
<main class="canvas">
  <section class="label">
    <div class="rose-illustration" role="img" aria-label="Illustration of a red rose with green leaves and rosebuds"></div>

    <svg class="label-frame" width="1000" height="1000" viewBox="0 0 1000 1000" aria-hidden="true">
      <polyline points="927,328 927,62 46,62 46,940 106,940" fill="none" stroke="var(--frame)" stroke-width="9"/>
    </svg>

    <div class="brand">
      <span class="brand-mark"></span>
      <div class="brand-name">lunora</div>
    </div>

    <h1 class="product-name">Rose</h1>
    <div class="product-type">water</div>

    <div class="volume-tab">100ml</div>
  </section>
</main>
</body>
</html>
```